CFO services graphic design

I own a business consulting firm called Hollins Advisory and we need a graphic for CFO services in our colours and branding. The attached file "CFO services to be put into Hollins advisory theme", shows the content for the design. The two other files show the theme and colours for the new design.

```html
<!DOCTYPE html>
<html lang="en">
<head>
<meta charset="utf-8">
<title>Chief Financial Officer Services</title>
<link rel="stylesheet" href="https://fonts.googleapis.com/css2?family=Encode+Sans+Semi+Condensed:wght@600;700&family=Montserrat:wght@800&display=swap">
<style>
  :root {
    --navy: #133a84;
    --sky: #0db0f2;
    --orange: #f7942a;
    --paper: #ffffff;
  }
  html, body {
    margin: 0;
    padding: 0;
    width: 1145px;
    height: 1200px;
    overflow: hidden;
    background: var(--paper);
  }
  .cfo-diagram {
    display: block;
    width: 1145px;
    height: 1200px;
  }
  .hub { fill: var(--sky); }
  .hub-title {
    fill: var(--paper);
    font-family: "Montserrat", sans-serif;
    font-weight: 800;
    font-size: 40px;
    letter-spacing: 1.5px;
  }
  .orbit { fill: none; stroke: var(--navy); stroke-width: 14; }
  .orbit-gap { fill: var(--paper); }
  .node-dot { fill: var(--navy); }
  .spoke { stroke: var(--navy); stroke-width: 14; }
  .service-arc { fill: none; stroke-width: 14; }
  .service-arc--warm { stroke: var(--orange); }
  .service-arc--cool { stroke: var(--sky); }
  .service-face { fill: var(--paper); }
  .service-label {
    fill: var(--navy);
    font-family: "Encode Sans Semi Condensed", sans-serif;
    font-weight: 700;
    text-anchor: middle;
    dominant-baseline: central;
  }
  .service-label .lead { font-size: 29px; }
  .service-label .detail { font-size: 24px; font-weight: 700; }
</style>
</head>
<body>
<svg class="cfo-diagram" viewBox="0 0 1870 1960" xmlns="http://www.w3.org/2000/svg" role="img" aria-label="Chief Financial Officer services: eight areas of responsibility">
  <defs>
    <g id="service-ring">
      <circle class="service-face" r="155"/>
      <path class="service-arc service-arc--warm" d="M0,-155 A155,155 0 0 0 0,155"/>
      <path class="service-arc service-arc--cool" d="M0,-155 A155,155 0 0 1 0,155"/>
    </g>
  </defs>

  <g class="spokes">
    <line class="spoke" x1="938" y1="617" x2="938" y2="668"/>
    <line class="spoke" x1="1196" y1="725" x2="1160" y2="761"/>
    <line class="spoke" x1="1304" y1="983" x2="1252" y2="983"/>
    <line class="spoke" x1="1196" y1="1241" x2="1160" y2="1205"/>
    <line class="spoke" x1="938" y1="1349" x2="938" y2="1298"/>
    <line class="spoke" x1="680" y1="1241" x2="716" y2="1205"/>
    <line class="spoke" x1="572" y1="983" x2="624" y2="983"/>
    <line class="spoke" x1="680" y1="725" x2="716" y2="761"/>
  </g>

  <circle class="orbit" cx="938" cy="983" r="290"/>
  <g class="orbit-gaps">
    <circle class="orbit-gap" cx="938" cy="693" r="22"/>
    <circle class="orbit-gap" cx="1143" cy="778" r="22"/>
    <circle class="orbit-gap" cx="1228" cy="983" r="22"/>
    <circle class="orbit-gap" cx="1143" cy="1188" r="22"/>
    <circle class="orbit-gap" cx="938" cy="1273" r="22"/>
    <circle class="orbit-gap" cx="733" cy="1188" r="22"/>
    <circle class="orbit-gap" cx="648" cy="983" r="22"/>
    <circle class="orbit-gap" cx="733" cy="778" r="22"/>
  </g>
  <g class="node-dots">
    <circle class="node-dot" cx="938" cy="693" r="11"/>
    <circle class="node-dot" cx="1143" cy="778" r="11"/>
    <circle class="node-dot" cx="1228" cy="983" r="11"/>
    <circle class="node-dot" cx="1143" cy="1188" r="11"/>
    <circle class="node-dot" cx="938" cy="1273" r="11"/>
    <circle class="node-dot" cx="733" cy="1188" r="11"/>
    <circle class="node-dot" cx="648" cy="983" r="11"/>
    <circle class="node-dot" cx="733" cy="778" r="11"/>
  </g>

  <circle class="hub" cx="938" cy="983" r="242"/>
  <text class="hub-title" x="938" text-anchor="middle">
    <tspan x="938" y="968">CHIEF FINANCIAL</tspan>
    <tspan x="938" y="1018">OFFICER</tspan>
  </text>

  <g class="service" transform="translate(938 455)">
    <use href="#service-ring"/>
    <text class="service-label"><tspan class="lead" style="font-size:27px" x="0" y="-34">COST ACCOUNTING</tspan><tspan class="lead" style="font-size:27px" x="0" y="-2">&amp; COST</tspan><tspan class="lead" style="font-size:27px" x="0" y="30">MANAGEMENT</tspan></text>
  </g>

  <g class="service" transform="translate(1311 610)">
    <use href="#service-ring"/>
    <text class="service-label"><tspan class="lead" x="-5" y="-57">CAPITAL</tspan><tspan class="lead" x="-5" y="-22">STRUCTURE</tspan><tspan class="lead" x="-5" y="13">AND THE</tspan><tspan class="lead" x="0" y="48">COST OF CAPITAL</tspan></text>
  </g>

  <g class="service" transform="translate(1466 983)">
    <use href="#service-ring"/>
    <text class="service-label"><tspan class="lead" x="0" y="-55">LONG-TERM &amp;</tspan><tspan class="lead" x="0" y="-20">SHORT-TERM</tspan><tspan class="lead" x="0" y="15">INVESTMENT</tspan><tspan class="lead" x="-5" y="50">DECISIONS</tspan></text>
  </g>

  <g class="service" transform="translate(1311 1356)">
    <use href="#service-ring"/>
    <text class="service-label"><tspan class="lead" x="0" y="-19">PERFORMANCE</tspan><tspan class="lead" x="0" y="16">EVALUATION</tspan></text>
  </g>

  <g class="service" transform="translate(938 1510)">
    <use href="#service-ring"/>
    <text class="service-label"><tspan class="lead" x="0" y="-36">BUDGETING &amp;</tspan><tspan class="lead" x="0" y="-1">STRATEGIC</tspan><tspan class="lead" x="0" y="34">PLANNING</tspan></text>
  </g>

  <g class="service" transform="translate(565 1356)">
    <use href="#service-ring"/>
    <text class="service-label"><tspan class="lead" x="-5" y="-19">RISK</tspan><tspan class="lead" x="0" y="16">MANAGEMENT</tspan></text>
  </g>

  <g class="service" transform="translate(410 983)">
    <use href="#service-ring"/>
    <text class="service-label"><tspan class="lead" x="0" y="-37">COMPLIACE:</tspan><tspan class="detail" style="font-size:26px" x="0" y="-6">TAX, LEGAL</tspan><tspan class="detail" style="font-size:26px" x="0" y="24">&amp; REGULATORY</tspan></text>
  </g>

  <g class="service" transform="translate(565 610)">
    <use href="#service-ring"/>
    <text class="service-label"><tspan class="lead" style="font-size:28px" x="0" y="-55">COMMUNICATION:</tspan><tspan class="detail" style="font-size:23px" x="0" y="-28">BOARD OF DIRECTORS</tspan><tspan class="detail" style="font-size:23px" x="0" y="-1">CREDITORS, OWNERS</tspan><tspan class="detail" style="font-size:23px" x="0" y="26">INVESTORS, CREDIT</tspan><tspan class="detail" style="font-size:23px" x="0" y="53">RATING AGENCIES</tspan></text>
  </g>
</svg>
</body>
</html>
```